Redesign Home Page

We need a new home page with a white background. Our company provides singing instruction to students world wide, both in person and on line. We're looking for a very clean and open design with maximum white space. The main goal of the page will be to get users to sign up for our mailing list. The current site is www.kelvarsong.com. I think the new page can be a long page (scrolll down is ok), to allow for more white space while still using the text from the current page.
Updates

Project Deadline Extended
Reason: Hello to all Designers, I apologize for not giving feedback this weekend. We went out of town for the Memorial Day holiday and I had no internet. I will be extending the deadline to Thursday. -Marcus

Target Market(s)

Singers of all ages and abilities, especially beginners.

Industry/Entity Type

It Company

Requirements
Must have
• 1. A white background
2. Lots of open space
3. An email sign up form on the top right that reads:
a. “Improve Your Singing Now.
b. Sign up for our Free Video Series: Tone Pathway
4. Testimonails: found on https://www.kelvarsong.com/tone-ascent
5. My logo with the piano
6. My photo
7. Learn about our Lessons in:
a. San Francisco
b. Alameda
8. On Line Programs:
a. Tone Ascent
b. Zelvo Lessons

Nice to have
• Link to current student page: http://kelvarsong.com/what-students-say/students2
Pictures of singers
Video box: Use Marcus_Example
Should not have
• See "KelvarSong Redesign" file for more details.

```html
<!DOCTYPE html>
<html lang="en">
<head>
<meta charset="utf-8">
<title>Marcus Hollin School of Voice</title>
<link href="https://fonts.googleapis.com/css2?family=Ubuntu:wght@400;500&family=Open+Sans:wght@400;600;700&display=swap" rel="stylesheet">
<style>
:root{
  --blue:#2e9fd8;
  --blue-dark:#1b86c2;
  --blue-deep:#177bb4;
  --heading:#2a9ad6;
  --text:#6b6b6b;
  --muted:#8a8a8a;
  --rule:#e6e6e6;
  --band:#efefef;
  --footer:#2b2b2b;
  --white:#ffffff;
}
*{box-sizing:border-box;margin:0;padding:0}
html,body{width:1200px;height:3154px;overflow:hidden;background:var(--white)}
body{position:relative;font-family:"Open Sans",Arial,sans-serif;color:var(--text)}
.abs{position:absolute}

/* header */
.site-header{position:absolute;left:0;top:0;width:1200px;height:170px}
.brand{position:absolute;left:87px;top:58px;display:flex;align-items:center;gap:16px}
.brand-mark{width:60px;height:60px;background:var(--blue);border-radius:50%}
.brand-name{font-family:"Ubuntu",sans-serif;font-size:38px;line-height:1;color:#666;font-weight:400}
.brand-tag{font-family:"Ubuntu",sans-serif;font-size:19px;color:#666;margin-top:6px;padding-left:26px}
.account{position:absolute;left:837px;top:85px;font-size:15px;color:#444}
.sign-in{position:absolute;left:997px;top:74px;width:116px;height:44px;background:var(--blue);color:var(--white);font-size:15px;display:flex;align-items:center;justify-content:center;gap:10px;border-radius:2px}
.sign-in svg{width:10px;height:6px}

/* nav */
.main-nav{position:absolute;left:0;top:170px;width:1200px;height:58px;background:linear-gradient(#36a9e1,#2596d2)}
.main-nav ul{list-style:none;position:absolute;left:87px;top:0;height:58px;display:flex}
.main-nav li{height:58px;display:flex;align-items:center;justify-content:center;color:var(--white);font-size:14px;font-weight:700;text-transform:uppercase;border-right:1px solid rgba(255,255,255,.25)}
.main-nav li:last-child{border-right:none}
.main-nav li.active{background:var(--blue-deep)}

/* hero */
.hero{position:absolute;left:0;top:228px;width:1200px;height:432px;background:linear-gradient(180deg,#ffffff 0%,#f4f4f4 60%,#ececec 100%);border-bottom:1px solid #e2e2e2}
.hero-title{position:absolute;left:129px;top:84px;font-family:"Ubuntu",sans-serif;font-size:29px;color:var(--heading);font-weight:400}
.hero-rule{position:absolute;left:129px;top:140px;width:416px;height:1px;background:#d9d9d9}
.field{position:absolute;left:129px;width:416px;height:44px;border:1px solid #cfcfcf;border-radius:3px;background:var(--white);font-size:13px;color:#555;padding:0 14px;display:flex;align-items:center}
.get-started-dark{position:absolute;left:390px;top:288px;width:155px;height:42px;background:#3a3a3a;color:var(--white);font-size:15px;display:flex;align-items:center;justify-content:center;border-radius:2px;box-shadow:0 2px 3px rgba(0,0,0,.3)}
.hero-photo{position:absolute;left:776px;top:45px;width:295px;height:387px;background:linear-gradient(160deg,#d9b8a4 0%,#6b4433 35%,#2e7a5a 70%,#1f5c45 100%);border-radius:140px 140px 0 0}
.dots{position:absolute;display:flex;gap:5px}
.dots span{width:15px;height:15px;border-radius:50%;background:#d0d0d0}
.dots span.on{background:#a6a6a6}

/* feature rows */
.photo{position:absolute}
.feature-title{position:absolute;font-family:"Ubuntu",sans-serif;font-size:29px;color:var(--heading);font-weight:400}
.feature-text{position:absolute;font-size:13.3px;line-height:23px;color:var(--text)}
.btn{position:absolute;height:44px;background:var(--blue-dark);border:2px solid var(--blue-dark);box-shadow:inset 0 0 0 2px var(--white);color:var(--white);font-size:17px;display:flex;align-items:center;justify-content:center}
.divider{position:absolute;left:87px;width:1026px;height:2px;background:var(--rule)}
.channel-dot{position:absolute;width:30px;height:30px;border-radius:50%;background:var(--blue)}

/* consultation */
.consult{position:absolute;left:0;top:1806px;width:1200px;height:356px;background:var(--band)}

/* testimonials */
.testimonials{position:absolute;left:0;top:2588px;width:1200px;height:446px;background:linear-gradient(180deg,#e3e3e3,#d4d4d4 50%,#e6e6e6)}
.testimonials .wash{position:absolute;inset:0;background:rgba(255,255,255,.55)}
.t-title{position:absolute;left:0;top:46px;width:1200px;text-align:center;font-family:"Ubuntu",sans-serif;font-size:33px;color:var(--heading)}
.avatar{position:absolute;left:529px;top:124px;width:142px;height:142px;border-radius:50%;background:linear-gradient(160deg,#c9a48c,#6e4a3a);border:4px solid var(--white)}
.quote{position:absolute;left:0;top:300px;width:1200px;text-align:center;font-size:16px;font-style:italic;color:#555}
.cite{position:absolute;left:0;top:346px;width:1200px;text-align:center;font-size:15px;color:#444}

/* footer */
.site-footer{position:absolute;left:0;top:3034px;width:1200px;height:120px;background:var(--footer);color:#e8e8e8;font-size:13px}
.footer-links{position:absolute;left:107px;top:36px}
.copyright{position:absolute;left:107px;top:72px}
.social{position:absolute;left:903px;top:44px;display:flex;gap:12px}
.social span{width:36px;height:36px;display:block}
</style>
</head>
<body>

<header class="site-header">
  <div class="brand">
    <span class="brand-mark" aria-hidden="true"></span>
    <div>
      <div class="brand-name">Marcus Hollin</div>
      <div class="brand-tag">School of Voice</div>
    </div>
  </div>
  <div class="account">Have an Account?</div>
  <div class="sign-in">Sign In
    <svg viewBox="0 0 10 6"><path d="M0 0h10L5 6z" fill="#fff"/></svg>
  </div>
</header>

<nav class="main-nav">
  <ul>
    <li class="active" style="width:105px">Home</li>
    <li style="width:186px">Voice Lessons</li>
    <li style="width:234px">What Students Say</li>
    <li style="width:249px">Meet the Instructors</li>
    <li style="width:252px">Tone Ascent</li>
  </ul>
</nav>

<section class="hero">
  <h1 class="hero-title">Sign Up For Our Free Video Series</h1>
  <div class="hero-rule"></div>
  <div class="field" style="top:168px">Name</div>
  <div class="field" style="top:225px">Email</div>
  <div class="get-started-dark">GET STARTED</div>
  <div class="hero-photo" role="img" aria-label="Photo of a smiling young woman wearing headphones"></div>
  <div class="dots" style="left:560px;top:390px"><span class="on"></span><span></span><span></span><span></span></div>
</section>

<!-- Alameda -->
<div class="photo" role="img" aria-label="Photo of a boat on the bay with the Alameda skyline" style="left:87px;top:750px;width:337px;height:218px;background:linear-gradient(180deg,#b9d4ea 0%,#9fb7c7 45%,#3c4b57 60%,#2f6f9e 75%,#2a5f8a 100%)"></div>
<h2 class="feature-title" style="left:487px;top:745px">Alameda</h2>
<p class="feature-text" style="left:487px;top:798px;width:626px">Typi non habent claritatem insitam; est usus legentis in iis qui facit eorum claritatem. Investigationes demonstraverunt lectores legere me lius quod ii legunt saepius. Claritas est etiam processus dynamicus, qui sequitur mutationem consuetudium lectorum. Mirum est notare quam littera gothica, quam nunc putamus parum claram, anteposuerit litterarum formas humanitatis per seacula quarta decima.</p>
<div class="btn" style="left:487px;top:918px;width:162px">Get Started</div>

<div class="divider" style="top:1042px"></div>

<!-- San Francisco -->
<h2 class="feature-title" style="left:87px;top:1104px">San Francisco</h2>
<p class="feature-text" style="left:87px;top:1157px;width:640px">Typi non habent claritatem insitam; est usus legentis in iis qui facit eorum claritatem. Investigationes demonstraverunt lectores legere me lius quod ii legunt saepius. Claritas est etiam processus dynamicus, qui sequitur mutationem consuetudium lectorum. Mirum est notare quam littera gothica, quam nunc putamus parum claram, anteposuerit litterarum formas humanitatis per seacula quarta decima.</p>
<div class="btn" style="left:87px;top:1279px;width:160px">Get Started</div>
<div class="photo" role="img" aria-label="Night photo of a lit bridge and the San Francisco skyline" style="left:776px;top:1110px;width:337px;height:217px;background:linear-gradient(135deg,#1a2340 0%,#3a3f6a 40%,#8a4a3a 65%,#1b2a4a 100%)"></div>

<div class="divider" style="top:1400px"></div>

<!-- Online -->
<div class="photo" role="img" aria-label="Photo of a young woman with headphones lying on the floor with a laptop" style="left:87px;top:1443px;width:383px;height:295px;background:radial-gradient(ellipse at 55% 55%,#e8c7b0 0%,#d98aa0 30%,#6f7f9a 55%,#ffffff 80%)"></div>
<span class="channel-dot" style="left:588px;top:1484px" aria-hidden="true"></span>
<h2 class="feature-title" style="left:638px;top:1478px">Online</h2>
<p class="feature-text" style="left:590px;top:1532px;width:523px">Typi non habent claritatem insitam; est usus legentis in iis qui facit eorum claritatem. Demonstraverunt lectores legere me lius quod ii legunt saepius. Claritas est etiam processus dynamicus, qui sequitur mutationem consuetudium lectorum. Mirum est notare quam littera gothica, quam nunc putamus parum claram, anteposuerit.</p>
<div class="btn" style="left:590px;top:1653px;width:160px">Get Started</div>

<!-- Consultation -->
<section class="consult">
  <h2 class="feature-title" style="left:118px;top:93px">Free Consultation With Marcus</h2>
  <p class="feature-text" style="left:118px;top:148px;width:580px">Marcus Hollin has openings for a free 15 minute consultation over the phone. If you have questions about your voice, click here to set up your time slot.</p>
  <div class="btn" style="left:118px;top:236px;width:160px">Get Started</div>
  <div class="photo" role="img" aria-label="Portrait photo of Marcus Hollin in a black turtleneck" style="left:763px;top:37px;width:328px;height:319px;background:linear-gradient(180deg,#efefef 0%,#c9a28a 20%,#b78a72 45%,#1e1e1e 62%,#111 100%);border-radius:150px 150px 0 0"></div>
</section>

<!-- Tone Ascent -->
<div class="photo" role="img" aria-label="Video player preview for the Tone Ascent lesson series" style="left:87px;top:2269px;width:337px;height:219px;background:linear-gradient(160deg,#5a5a5a 0%,#1a1a1a 45%,#0b2b4a 75%,#121212 100%)"></div>
<h2 class="feature-title" style="left:487px;top:2269px">Tone Ascent</h2>
<p class="feature-text" style="left:487px;top:2322px;width:626px">Tone Ascent is a Video Series designed to give you all the techniques you need to fully develop your singing voice. With 30 videos, sixty audio workouts, and an eBook, the platform is the most advanced you'll find anywhere. Click here for more information.</p>
<div class="btn" style="left:487px;top:2433px;width:162px">Click Here</div>

<!-- Testimonials -->
<section class="testimonials" role="img" aria-label="Faded grid of student portrait photos behind the testimonial">
  <div class="wash"></div>
  <h2 class="t-title">Loved by over 100,000 people worldwide</h2>
  <div class="avatar" role="img" aria-label="Portrait photo of Dara Whitcomb"></div>
  <p class="quote">I would recommend this Theme to anyone who wants to have an awesome app landing page for their apps or products.</p>
  <p class="cite">Dara Whitcomb - vantelo.com</p>
  <div class="dots" style="left:560px;top:394px"><span class="on"></span><span></span><span></span><span></span></div>
</section>

<footer class="site-footer">
  <div class="footer-links">Terms and Conditions | Privacy Promise | FAQ's | Contact Us</div>
  <div class="copyright">Copyright © 2013. All Rights Reserved.</div>
  <div class="social">
    <span style="background:#3b5a9a" aria-label="Social link"></span>
    <span style="background:#2a9fd8" aria-label="Social link"></span>
    <span style="background:#ef7d22" aria-label="Social link"></span>
    <span style="background:#d8262b" aria-label="Social link"></span>
  </div>
</footer>

</body>
</html>
```